Stationery for Villa Marejada Design Hotel**

Who we are:

Wander on an isolated beach while breathing in the fresh, salty, sea air. Listen to the warm Pacific wind rustling through green palm trees as you walk to a pristine lagoon. Feel the delicious warmth of the sun kiss your skin; the beach is yours. At Villa Marejada you can experience a vacation in undisturbed, natural beauty. We have created a place for you to find new strength, relaxation, and inner harmony. We offer total rest to the experienced traveler from all over the world.

We are a brand new and smartly built design-hotel (under construction) close to a unique beach and a fantastic surf spot in Huatulco, Southwest Mexico.

As you can see in the attachments, we do have an established corporate design, but as for now still need a format for booklets for information around our hotel and things to do in the area, important numbers (we fill in the content for that one).

Our corporate colors:
green #64b445, brown #b07043, blue #0ab7cf, yellow # f9b02a and #fcc01a, navy #444f69
Corporate fonts:
Krub and Miller Banner.
For further information access:
www.villamarejada.example
https://slideshare.example/view/QxLmPwTr8KdNvYsZhJcA/

Social Media: VillaMarejada

Industry/Entity Type

Hotel

Font styles to use
Other font styles liked:
• Krub, Miller Banner

Requirements
Must have
• Stick to Logo Design, defined corporate elements, logo, colors, fonts and general touch and feel
Nice to have
• Who we are:

Our corporate colors:
Corporate fonts:
Krub and Miller Banner.
www.villamarejada.example

Social Media: VillaMarejada

```html
<!DOCTYPE html>
<html lang="en">
<head>
<meta charset="utf-8">
<title>Villa Marejada – Business Card</title>
<link rel="stylesheet" href="https://fonts.googleapis.com/css2?family=Krub:wght@400;500;600&family=Gelasio:wght@700&display=swap">
<style>
  :root {
    --green: #64b445;
    --navy: #444f69;
    --ink: #3e4660;
    --gold: #d9a92a;
    --backdrop: #ececec;
    --paper: #ffffff;
  }
  * { box-sizing: border-box; margin: 0; padding: 0; }
  html, body {
    width: 1188px; height: 1200px; overflow: hidden;
    background: var(--backdrop);
  }
  .sheet { position: relative; width: 1188px; height: 1200px; }
  .card {
    position: absolute; left: 245px; width: 696px; height: 386px;
    font-family: "Krub", sans-serif;
  }
  .card--front { top: 159px; background: var(--paper); color: var(--ink); }
  .card--back { top: 627px; background: var(--navy); }

  .person { position: absolute; left: 65px; top: 96px; }
  .person__name {
    font-family: "Gelasio", Georgia, serif; font-weight: 700;
    font-size: 28px; line-height: 1.1; color: var(--green);
  }
  .person__role { font-size: 19px; line-height: 1.2; }

  .address {
    position: absolute; left: 65px; top: 208px;
    font-style: normal; font-size: 17.5px; line-height: 21.5px;
  }
  .contact {
    position: absolute; left: 65px; top: 288px;
    font-size: 17.5px; line-height: 24px; list-style: none;
  }
  .contact__label { color: var(--green); font-weight: 500; margin-right: 4px; }
  .website {
    position: absolute; right: 64px; top: 312px;
    font-size: 17.5px; line-height: 24px;
  }
  .website__name { color: var(--green); }

  .brandmark {
    position: absolute; display: flex; flex-direction: column; align-items: center;
  }
  .brandmark__square { background: var(--gold); }
  .brandmark__name {
    font-family: "Krub", sans-serif; font-weight: 600; color: var(--gold);
    letter-spacing: 0.04em; text-transform: uppercase; white-space: nowrap;
  }
  .card--front .brandmark { left: 496px; top: 54px; width: 140px; }
  .card--front .brandmark__square { width: 110px; height: 108px; }
  .card--front .brandmark__name { font-size: 15px; margin-top: 10px; }
  .card--back .brandmark { left: 198px; top: 66px; width: 300px; }
  .card--back .brandmark__square { width: 196px; height: 190px; }
  .card--back .brandmark__name { font-size: 29px; margin-top: 8px; }
</style>
</head>
<body>
<main class="sheet">
  <section class="card card--front">
    <div class="person">
      <h1 class="person__name">Lucia Ferrand</h1>
      <p class="person__role">Founder</p>
    </div>
    <address class="address">
      Villa Marejada<br>
      Playa Serena, Puerto Lumen<br>
      Valle Claro, Marelia
    </address>
    <ul class="contact">
      <li><span class="contact__label">T :</span>+52 1 (555) 010 4821</li>
      <li><span class="contact__label">E :</span>hello@villamarejada.example</li>
    </ul>
    <p class="website">www.<span class="website__name">villamarejada</span>.example</p>
    <div class="brandmark">
      <div class="brandmark__square"></div>
      <p class="brandmark__name">Villa Marejada</p>
    </div>
  </section>

  <section class="card card--back">
    <div class="brandmark">
      <div class="brandmark__square"></div>
      <p class="brandmark__name">Villa Marejada</p>
    </div>
  </section>
</main>
</body>
</html>
```